Killer design for artists website and gallery

Current website is www.bluemoorstudio.com.au and it runs on a very simple Wordpress standard theme. We would like a theme designed and customised to suit the branding and style. We have someone who will then code the site in HTML and CSS into Wordpress.

The general theme and branding can be seen on the site at the moment. Please note I have now uploaded full size files into the project. The website background files are for reference only as they are currently on the site. There is no requirement to use them in the new design, however the logo must be as per the attachment.. Please submit a home page/main gallery, and we will request additional pages (about us, other galleries etc.) from those designers we like during the project time.
Updates

Please note I have now uploaded full size files into the project. The website background files are for reference only as they are currently on the site. There is no requirement to use them in the new design, however the logo must be as per the attachment.

Target Market(s)

sales are only in Australia, and priced between approx $100 and $1000. Most viewers and buyers are 20-40 years old, and looking for a casual canvas work for home, or a gift.

Industry/Entity Type

Artists

Font styles to use
Serif
Sans Serif

Requirements
Must have
• gallery of images, responsive design, ability to select categories of pictures (see top menu on current site) and have the gallery change to match, colours to match branding and logo.
Nice to have
• simple minimalist style is preferred. More like http://www.tobiasmerrow.com/ than http://www.harbourpaintco.com.au/ or http://www.velvetcanvas.com.au/
Should not have
• does not need any online store, or shopping cart etc.

```html
<!DOCTYPE html>
<html lang="en">
<head>
<meta charset="utf-8">
<title>Bluemoor Studio – Testimonials</title>
<link rel="stylesheet" href="https://fonts.googleapis.com/css2?family=Open+Sans:wght@400;700&family=Lato:ital,wght@0,400;0,700;1,400&display=swap">
<style>
:root{
  --ink:#111111;
  --accent:#f2e800;
  --accent-text:#e6dc00;
  --rule:#d6d6d6;
  --muted:#a8a8a8;
  --paper:#ffffff;
  --haze:#f2f2f2;
  --btn-border:#c9c9c9;
  --btn-fill:#f4f4f4;
}
*{margin:0;padding:0;box-sizing:border-box}
html,body{width:1200px;height:810px;overflow:hidden;background:var(--paper)}
body{position:relative;font-family:'Open Sans',Arial,sans-serif;color:var(--ink)}
.backdrop{position:absolute;right:0;top:0;width:560px;height:780px;
  background:radial-gradient(ellipse at 75% 45%,var(--haze) 0%,rgba(242,242,242,0) 70%)}
.brand{position:absolute;top:36px;left:0;width:1200px;display:flex;justify-content:center;align-items:center;gap:10px}
.brand-mark{width:22px;height:22px;background:var(--ink);border:2px solid var(--accent)}
.brand-name{font-size:22px;font-weight:700;letter-spacing:1px;text-transform:uppercase}
.top-social{position:absolute;top:15px;left:957px;display:flex;gap:5px}
.top-social span{width:19px;height:19px;border:1.5px solid var(--ink);border-radius:50%}
.search{position:absolute;top:58px;left:838px;width:162px;height:22px;border:1px solid var(--rule);display:flex;justify-content:flex-end}
.search-btn{width:20px;border-left:1px solid var(--rule);display:flex;align-items:center;justify-content:center}
.main-nav{position:absolute;top:116px;left:0;width:1200px;display:flex;justify-content:center;gap:24px;font-size:12px;text-transform:uppercase;letter-spacing:.2px}
.main-nav .current{color:var(--accent-text)}
.nav-rule{position:absolute;top:144px;left:0;width:1200px;border-top:1px solid var(--rule)}
.page-title{position:absolute;top:172px;left:201px;font-size:29px;font-weight:700;line-height:36px}
.title-bar{position:absolute;top:214px;left:199px;width:191px;height:6px;background:var(--accent)}
.testimonial{position:absolute;left:199px;width:800px;display:flex;gap:16px}
.portrait{width:74px;height:74px;flex:none;border:2px solid var(--accent);border-radius:5px}
.p1{background:linear-gradient(135deg,#d9d9d9,#8a8a8a)}
.p2{background:linear-gradient(135deg,#c8392b,#6a2c6e 60%,#d9b03a)}
.p3{background:linear-gradient(135deg,#8a7650,#e8ddc6 55%,#4d3b22)}
.quote{font-family:'Lato',Arial,sans-serif;font-style:italic;font-size:12.6px;line-height:15.5px;margin-top:10px;width:705px}
.cite{font-family:'Lato',Arial,sans-serif;font-style:italic;font-size:12.6px;color:var(--accent-text);margin-top:9px}
.cite .date{color:var(--ink);margin-left:4px}
.action-bar{position:absolute;top:558px;left:0;width:1200px;height:40px;border-top:1px solid var(--rule);border-bottom:1px solid var(--rule)}
.action-label{position:absolute;top:11px;font-family:'Lato',Arial,sans-serif;font-weight:700;font-size:13px}
.stars{position:absolute;top:11px;left:264px;display:flex;gap:2px}
.share{position:absolute;top:10px;left:548px;display:flex;gap:5px}
.share-btn{height:17px;border:1px solid var(--btn-border);background:var(--btn-fill);font-size:9.5px;color:#444;display:flex;align-items:center;gap:4px;padding:0 4px}
.share-btn i{width:11px;height:11px;display:block}
.likes{position:absolute;top:12px;left:934px;display:flex;gap:12px}
.likes span{width:14px;height:14px;border-radius:50%}
.footer-divider{position:absolute;top:605px;left:0}
.footer-nav{position:absolute;top:663px;left:0;width:1200px;display:flex;justify-content:center;gap:24px;font-size:12px;text-transform:uppercase;color:var(--muted)}
.copyright{position:absolute;top:712px;left:0;width:1200px;text-align:center;font-size:10.5px;color:#444}
.footer-brand{position:absolute;top:716px;right:200px;display:flex;align-items:center;gap:6px}
.footer-brand .brand-mark{width:14px;height:14px;border:none;background:#333}
.footer-brand .brand-name{font-size:13px;color:#333}
.footer-social{position:absolute;top:771px;left:940px;display:flex;gap:6px}
.footer-social span{width:13px;height:13px;border-radius:50%;background:#333}
</style>
</head>
<body>
<div class="backdrop" role="img" aria-label="Faint grey tree branches spreading across the background"></div>

<header>
  <div class="brand"><span class="brand-mark"></span><span class="brand-name">Bluemoor Studio</span></div>
  <div class="top-social"><span></span><span></span></div>
  <div class="search"><div class="search-btn">
    <svg width="10" height="10" viewBox="0 0 10 10"><circle cx="4" cy="4" r="3" fill="none" stroke="#111" stroke-width="1.2"/><line x1="6.2" y1="6.2" x2="9" y2="9" stroke="#111" stroke-width="1.4"/></svg>
  </div></div>
  <nav class="main-nav">
    <span>Home</span><span>About</span><span>Cityscapes</span><span>Other Works</span><span>Seacapes</span><span class="current">Testimonials</span><span>Work for Sale</span>
  </nav>
  <div class="nav-rule"></div>
</header>

<main>
  <h1 class="page-title">Testomonials</h1>
  <div class="title-bar"></div>

  <article class="testimonial" style="top:239px">
    <div class="portrait p1" role="img" aria-label="Pencil portrait artwork thumbnail"></div>
    <div>
      <p class="quote">“Ella did an outstanding job painting a scene from my hometown. She captured the essence of the city perfectly and it takes pride of place in my living room. I highly recommend you employ Ella Bluemoor’s talents, I certainly will in the future”</p>
      <p class="cite">Daniel Corrigan, Melbourne, <span class="date">Feburay 2014</span></p>
    </div>
  </article>

  <article class="testimonial" style="top:349px">
    <div class="portrait p2" role="img" aria-label="Colourful painted portrait thumbnail"></div>
    <div>
      <p class="quote">“Ella did an outstanding job painting a scene from my hometown. She captured the essence of the city perfectly and it takes pride of place in my living room. I highly recommend you employ Ella Bluemoor’s talents, I certainly will in the future”</p>
      <p class="cite">Daniel Corrigan, Melbourne, May 2012</p>
    </div>
  </article>

  <article class="testimonial" style="top:460px">
    <div class="portrait p3" role="img" aria-label="Classical oil portrait thumbnail"></div>
    <div>
      <p class="quote">“Ella did an outstanding job painting a scene from my hometown. She captured the essence of the city perfectly and it takes pride of place in my living room. I highly recommend you employ Ella Bluemoor’s talents, I certainly will in the future”</p>
      <p class="cite">Daniel Corrigan, Melbourne, May 2012</p>
    </div>
  </article>

  <section class="action-bar">
    <span class="action-label" style="left:201px">Rate this:</span>
    <div class="stars">
      <svg width="78" height="16" viewBox="0 0 78 16">
        <defs><polygon id="star" points="8,0 10,5.6 16,5.8 11.2,9.4 13,15.5 8,11.8 3,15.5 4.8,9.4 0,5.8 6,5.6"/></defs>
        <use href="#star" x="0" fill="#f2e800"/>
        <use href="#star" x="19" fill="#f2e800"/>
        <use href="#star" x="38" fill="#f2e800"/>
        <use href="#star" x="57" fill="#111"/>
      </svg>
    </div>
    <span class="action-label" style="left:466px">Share this:</span>
    <div class="share">
      <span class="share-btn"><i style="background:#4fb6e8"></i>Chirper</span>
      <span class="share-btn"><i style="background:#3b5a9a"></i>Facepage</span>
      <span class="share-btn"><i style="background:#d9503e"></i>Searchly</span>
    </div>
    <span class="action-label" style="left:868px">Like this:</span>
    <div class="likes"><span style="background:#3b5a9a"></span><span style="background:#2aa3e0"></span></div>
  </section>
</main>

<footer>
  <svg class="footer-divider" width="1200" height="32" viewBox="0 0 1200 32">
    <path d="M0 7 H578 L600 28 L622 7 H1200" fill="none" stroke="#d6d6d6" stroke-width="1.5" stroke-dasharray="6 4"/>
  </svg>
  <nav class="footer-nav">
    <span>Home</span><span>About</span><span>Cityscapes</span><span>Other Works</span><span>Seacapes</span><span>Testimonials</span><span>Work for Sale</span>
  </nav>
  <p class="copyright">© Copyright BluemoorStudio 2014</p>
  <div class="footer-brand"><span class="brand-mark"></span><span class="brand-name">Bluemoor Studio</span></div>
  <div class="footer-social"><span></span><span></span><span></span></div>
</footer>
</body>
</html>
```